Fahrzeugbeschriftung für Wohnmobil gesucht
Zielgruppe
Wir sind eine Familie und eines unserer Kinder fährt Rennkart. Dazu benötigen wir ein Wohnmobil, das in einem neuen Design erscheinen soll.
Beim Fahrzeug handelt es sich um einen Valdoro (Kessa) Arta 58 Max Teilintegriert (https://www.valdoro-xyz.it/ch/de/camper/gamma/arta/modello/58-max Bildervorlage kann hier bezogen werden)
Aufgabenstellung
Das Fahrzeug wird foliert, mit geschnittenen Folien. So sind Farbverläufe nicht möglich. Bestehende Folierung entfernt
Die Grundfarbe bleibt weiss
Es soll neben schwarz, hellblau verwendet werden und pink (dies aber dezent)
-Die Fenster auf der linken und rechts sollen in einem schwarzen 'Streifen' integriert werden, sodass sie weniger auffallen
- Es benötigt auf beiden Seiten und hinten 4 Felder (ca. 20x50cm) in weiss für Sponsorenlogos
- auf beiden Seiten soll die Nummer 164 stehen. Diese Nummer muss alleine stehen, dass sie getauscht werden kann
- ich habe noch ein Bild ergänzt, vielleicht ist dies eine Option auf die Rückseite
- der Fahrername ist Lenz Brügger

```html
<!DOCTYPE html>
<html lang="de">
<head>
<meta charset="utf-8">
<title>Wohnmobil Heckbeschriftung – Lenz Brügger</title>
<link rel="stylesheet" href="https://fonts.googleapis.com/css2?family=Jost:wght@500;600&display=swap">
<style>
  :root {
    --backdrop: #eef0f2;
    --body-white: #ffffff;
    --foil-black: #0b0b0b;
    --foil-lightblue: #9db8e0;
    --checker-tone: #5a5a5a;
    --bumper-grey: #e4e5e7;
    --light-red: #c8302c;
    --brake-red: #b33a36;
    --plate-white: #f7f7f7;
    --plate-blue: #2a4fa0;
    --type: "Jost", sans-serif;
  }
  html, body {
    margin: 0;
    padding: 0;
    overflow: hidden;
  }
  .canvas {
    position: relative;
    width: 1200px;
    height: 798px;
    background: var(--backdrop);
    overflow: hidden;
    font-family: var(--type);
  }
  .rear-panel {
    position: absolute;
    left: 382px;
    top: 154px;
    width: 465px;
    height: 495px;
    background: var(--body-white);
    border-radius: 18px 18px 10px 10px;
    box-shadow: 0 0 0 1px #d6d8db;
    overflow: hidden;
  }
  .rear-panel > * { position: absolute; }
  .brake-light {
    left: 179px; top: 16px;
    width: 70px; height: 10px;
    background: var(--brake-red);
    border-radius: 3px;
  }
  .sponsor-band {
    left: 0; top: 69px;
    width: 465px; height: 123px;
    background: var(--foil-black);
  }
  .brand-mark {
    left: 36px; top: 94px;
    width: 62px;
    display: flex; flex-direction: column; align-items: center; gap: 5px;
    color: var(--body-white);
    font-weight: 600; font-size: 12px; letter-spacing: 0.5px;
    line-height: 1;
  }
  .brand-mark .brand-square {
    width: 36px; height: 36px;
    background: var(--body-white);
    border-radius: 4px;
  }
  .sponsor-field {
    width: 90px; height: 50px;
    background: var(--body-white);
    display: flex; align-items: center; justify-content: center;
    font-weight: 600; font-size: 15px; color: var(--foil-black);
  }
  .sponsor-field.s1 { left: 107px; top: 78px; }
  .sponsor-field.s2 { left: 207px; top: 78px; }
  .sponsor-field.s3 { left: 256px; top: 135px; }
  .sponsor-field.s4 { left: 358px; top: 135px; }
  .checker { background: var(--checker-tone); }
  .checker.left { left: 0; top: 192px; width: 135px; height: 107px; }
  .checker.right { left: 386px; top: 369px; width: 79px; height: 54px; }
  .kart-artwork {
    left: 62px; top: 202px;
    width: 225px; height: 197px;
    background: var(--foil-lightblue);
    border-radius: 30px 40px 24px 24px;
  }
  .driver-name {
    left: 295px; top: 226px;
    margin: 0;
    color: var(--foil-black);
    font-weight: 500; font-size: 22px;
    line-height: 1.1; letter-spacing: 4px;
    text-transform: uppercase;
  }
  .model-label {
    left: 351px; top: 370px;
    font-size: 8px; line-height: 1.1;
    color: var(--foil-black);
  }
  .bumper {
    left: 0; top: 430px;
    width: 465px; height: 65px;
    background: var(--bumper-grey);
  }
  .tail-light {
    top: 441px; width: 46px; height: 24px;
    background: var(--light-red);
    border-radius: 3px;
  }
  .tail-light.left { left: 25px; }
  .tail-light.right { left: 392px; }
  .number-plate {
    left: 192px; top: 444px;
    width: 86px; height: 18px;
    background: var(--plate-white);
    border-left: 6px solid var(--plate-blue);
    box-sizing: border-box;
    display: flex; align-items: center; justify-content: center;
    font-weight: 600; font-size: 10px; color: var(--foil-black);
    letter-spacing: 0.3px;
  }
</style>
</head>
<body>
<main class="canvas">
  <section class="rear-panel">
    <div class="brake-light"></div>
    <div class="sponsor-band"></div>
    <div class="brand-mark"><span class="brand-square"></span>VALDORO</div>
    <div class="sponsor-field s1">SPONS.</div>
    <div class="sponsor-field s2">SPONS.</div>
    <div class="sponsor-field s3">SPONS.</div>
    <div class="sponsor-field s4">SPONS.</div>
    <div class="checker left" role="img" aria-label="Schwarz-weisse Zielflaggen-Karos"></div>
    <div class="kart-artwork" role="img" aria-label="Hellblaue Illustration eines Fahrers im Rennkart"></div>
    <div class="checker right" role="img" aria-label="Schwarz-weisse Zielflaggen-Karos"></div>
    <h1 class="driver-name">Lenz<br>Brügger</h1>
    <div class="model-label">Arta<br>58 Max</div>
    <div class="bumper"></div>
    <div class="tail-light left"></div>
    <div class="tail-light right"></div>
    <div class="number-plate">VALDORO 22</div>
  </section>
</main>
</body>
</html>
```